Qualified Machining Operator Training Program

We need a flyer to advertise a training program to business. I will attach a rough draft "original file" that we need enhanced to look professional. Details to the program are here https://www.halvornskills.org/credentials/machining-credential-qmo/ We want it to look clean and professional.

Please use the information that is on the "original file" rough draft. I have attached an example pdf, the reason I don't like the example is because it has too many words and looks out of date.

Font styles to use
Serif
Sans Serif

```html
<!DOCTYPE html>
<html lang="en">
<head>
<meta charset="utf-8">
<title>Qualified Machining Operator Program – Flyer</title>
<link href="https://fonts.googleapis.com/css2?family=Open+Sans:wght@400;700&family=Poppins:wght@500;600&family=Questrial&family=Playfair+Display:wght@600&display=swap" rel="stylesheet">
<style>
  :root{
    --navy:#10105a;
    --navy-deep:#0c0c4a;
    --ink:#2b2b2b;
    --grey-title:#4a4a4a;
    --band:#575757;
    --band-dark:#3f3f3f;
    --white:#ffffff;
    --page:#ececec;
    --stripe:#6a6a6a;
  }
  *{margin:0;padding:0;box-sizing:border-box}
  html,body{width:1200px;height:1200px;overflow:hidden;background:var(--page)}
  .flyer{position:absolute;left:172px;top:0;width:856px;height:1200px;background:var(--white);overflow:hidden;font-family:"Questrial",sans-serif;color:var(--ink)}
  .abs{position:absolute}

  /* header */
  .header-band{left:0;top:0;width:856px;height:152px}
  .brand{left:40px;top:44px;width:260px;display:flex;align-items:center;gap:10px;font-family:"Playfair Display",serif;font-weight:600;font-size:38px;color:var(--navy);letter-spacing:1px}
  .brand-dot{width:18px;height:18px;border-radius:50%;background:var(--navy)}
  .contact{top:46px;font-family:"Poppins",sans-serif;color:var(--white);font-size:18px;display:flex;align-items:center;gap:7px}
  .contact.phone{left:380px;font-weight:600}
  .contact.mail{left:588px;font-weight:500;font-size:16px}
  .onsite{left:380px;top:78px;font-family:"Poppins",sans-serif;font-weight:600;font-size:30px;color:var(--white);white-space:nowrap}

  /* hero */
  .hero-photo{left:0;top:152px;width:856px;height:373px;background:linear-gradient(90deg,#8c8f98 0%,#9aa4bd 30%,#b9c2d8 48%,#e9ecf3 65%,#ffffff 76%)}
  .title{right:90px;top:0;text-align:right;font-family:"Open Sans",sans-serif;line-height:1}
  .title .light{position:absolute;right:0;font-size:58px;color:var(--grey-title);font-weight:400;white-space:nowrap}
  .title .bold{position:absolute;right:0;font-size:52px;color:var(--navy);font-weight:700;white-space:nowrap}

  /* skills */
  .skills{left:0;top:525px;width:856px;height:171px;background:linear-gradient(90deg,var(--band) 0%,var(--band-dark) 55%,var(--band) 100%)}
  .skills-head{left:0;top:14px;width:856px;display:flex;justify-content:center;align-items:center;gap:16px;font-family:"Poppins",sans-serif;font-weight:600;font-size:34px;color:var(--white);letter-spacing:.5px}
  .skills-head span.rule{width:52px;height:3px;background:var(--white)}
  .skill{color:#ececec;font-size:14.5px;line-height:17px;padding-left:14px}
  .skill::before{content:"";position:absolute;left:0;top:6px;width:6px;height:6px;border-radius:50%;background:#e0e0e0}

  /* pillars */
  .pillars{left:47px;top:717px;width:760px;height:98px}
  .pillar-label{font-family:"Poppins",sans-serif;font-weight:600;font-size:20px;color:var(--white);text-align:center;line-height:26px}
  .pillar-label.two-line{font-size:18px;line-height:24px}

  /* feature box */
  .feature{left:47px;top:834px;width:760px;height:173px;background:var(--navy)}
  .panel{background:var(--white)}
  .feature-lines{left:170px;top:41px;width:420px;text-align:center;font-family:"Poppins",sans-serif;font-weight:500;font-size:15.5px;color:var(--white);line-height:31px}
  .hours{right:12px;text-align:right;font-family:"Poppins",sans-serif;color:var(--ink);white-space:nowrap}

  /* quote */
  .quote{left:75px;top:1040px;width:706px;font-family:"Poppins",sans-serif;font-weight:500;font-size:11.3px;line-height:15px;text-align:justify;text-align-last:left;color:var(--ink)}
  .qmark{font-family:"Playfair Display",serif;font-weight:600;font-size:40px;color:var(--navy);line-height:1}

  /* partners */
  .partner{top:1115px;height:30px;display:flex;align-items:center;justify-content:center;font-family:"Poppins",sans-serif;font-weight:600;font-size:22px;color:var(--navy)}
  .badge{top:1112px}

  .footer{left:0;top:1160px;width:856px;height:40px}
</style>
</head>
<body>
<main class="flyer">

  <svg class="abs header-band" viewBox="0 0 856 152" aria-hidden="true">
    <polygon points="305,0 856,0 856,152 361,152 361,137" fill="var(--navy)"/>
    <rect x="0" y="137" width="856" height="15" fill="var(--navy)"/>
  </svg>
  <div class="abs brand"><span class="brand-dot"></span>HALVORN</div>
  <div class="abs contact phone">
    <svg width="16" height="16" viewBox="0 0 24 24" aria-hidden="true"><path fill="#fff" d="M6.6 10.8a15.1 15.1 0 0 0 6.6 6.6l2.2-2.2a1 1 0 0 1 1-.25 11.4 11.4 0 0 0 3.6.57 1 1 0 0 1 1 1V20a1 1 0 0 1-1 1A17 17 0 0 1 3 4a1 1 0 0 1 1-1h3.5a1 1 0 0 1 1 1c0 1.250.2 2.450.57 3.57a1 1 0 0 1-.25 1z"/></svg>
    555 014 7720
  </div>
  <div class="abs contact mail">
    <svg width="18" height="14" viewBox="0 0 24 18" aria-hidden="true"><rect x="0" y="0" width="24" height="18" rx="2" fill="#fff"/><path d="M1 2l11 8 11-8" stroke="var(--navy)" stroke-width="2" fill="none"/></svg>
    dana@northlinelean.com
  </div>
  <div class="abs onsite">On-site training available</div>

  <div class="abs hero-photo" role="img" aria-label="Photo of a hands-on training rig: motor, pneumatic lines and a blue control cabinet on a workbench, fading to white on the right">
    <div class="abs title">
      <span class="light" style="top:105px">Qualified</span>
      <span class="bold" style="top:177px">MACHINING</span>
      <span class="bold" style="top:236px">OPERATOR</span>
      <span class="light" style="top:295px">Program</span>
    </div>
  </div>

  <section class="abs skills">
    <div class="abs skills-head"><span class="rule"></span>SKILLS TAUGHT<span class="rule"></span></div>
    <div class="abs skill" style="left:47px;top:85px">Communication</div>
    <div class="abs skill" style="left:47px;top:114px">Lean Principles</div>
    <div class="abs skill" style="left:47px;top:143px">Problem Solving</div>
    <div class="abs skill" style="left:212px;top:85px">Total Productive<br>Maintenance</div>
    <div class="abs skill" style="left:212px;top:130px">Project<br>Management</div>
    <div class="abs skill" style="left:369px;top:85px">Locating<br>Information</div>
    <div class="abs skill" style="left:369px;top:130px">Supply Chain &amp;<br>Logistics</div>
    <div class="abs skill" style="left:519px;top:85px">Autonomous<br>Maintenance</div>
    <div class="abs skill" style="left:519px;top:130px">Total Productive<br>Maintenance</div>
    <div class="abs skill" style="left:676px;top:85px">Data Analysis</div>
    <div class="abs skill" style="left:676px;top:114px">Customer Service</div>
    <div class="abs skill" style="left:676px;top:143px">Teamwork</div>
  </section>

  <div class="abs pillars">
    <svg class="abs" style="left:0;top:0" width="760" height="98" viewBox="0 0 760 98" role="img" aria-label="Four dark photo-tinted chevrons: safety gear, quality inspection, machine processes, maintenance gears">
      <defs>
        <linearGradient id="chev" x1="0" y1="0" x2="1" y2="1">
          <stop offset="0" stop-color="#4a4237"/><stop offset="1" stop-color="#242424"/>
        </linearGradient>
      </defs>
      <polygon points="0,0 190,0 210,49 190,98 0,98" fill="url(#chev)"/>
      <polygon points="197,0 385,0 405,49 385,98 197,98 217,49" fill="url(#chev)"/>
      <polygon points="392,0 580,0 600,49 580,98 392,98 412,49" fill="url(#chev)"/>
      <polygon points="587,0 760,0 760,98 587,98 607,49" fill="url(#chev)"/>
    </svg>
    <div class="abs pillar-label" style="left:0;width:200px;top:36px">SAFETY</div>
    <div class="abs pillar-label" style="left:210px;width:185px;top:36px">QUALITY</div>
    <div class="abs pillar-label" style="left:405px;width:185px;top:36px">PROCESSES</div>
    <div class="abs pillar-label two-line" style="left:614px;width:140px;top:25px">MAINTENANCE<br>AWARENESS</div>
  </div>

  <section class="abs feature">
    <div class="abs panel" style="left:7px;top:9px;width:255px;height:155px" role="img" aria-label="Screenshot of interactive e-learning lesson with a pneumatic cylinder diagram"></div>
    <div class="abs feature-lines">Advanced Manufacturing<br>Hands-On Learning<br>College Credits Eligible</div>
    <div class="abs panel" style="left:496px;top:9px;width:254px;height:155px">
      <div class="abs" style="left:12px;top:8px;width:118px;height:138px;background:linear-gradient(160deg,#cdd3dc,#9aa6b6)" role="img" aria-label="Photo of the portable training rig with blue control cabinet"></div>
      <div class="abs hours" style="top:96px;font-size:20px;font-weight:600">120 hours</div>
      <div class="abs hours" style="top:124px;font-size:11.5px;font-weight:500">$2,500 per student</div>
      <div class="abs hours" style="top:139px;font-size:11.5px;font-family:'Questrial',sans-serif">STF Reimbursement</div>
    </div>
  </section>

  <div class="abs qmark" style="left:47px;top:1030px">&ldquo;</div>
  <p class="abs quote">we feel that Halvorn QMO certification compliments not only the qualifiations of the candidates we see, but also enhances the knowledge, skills, and abilities of existing team members in our pursuit of manufacturing excellence</p>
  <div class="abs qmark" style="left:790px;top:1068px">&rdquo;</div>

  <div class="abs partner" style="left:40px;width:100px">Verak</div>
  <div class="abs partner" style="left:200px;width:120px">Ostrana</div>
  <div class="abs badge" style="left:417px;width:32px;height:36px;background:#2f6b3a"></div>
  <div class="abs badge" style="left:578px;top:1115px;width:50px;height:30px;border-radius:50%;background:var(--navy)"></div>
  <div class="abs badge" style="left:752px;top:1108px;width:42px;height:42px;border-radius:50%;background:#8a93a3"></div>

  <svg class="abs footer" viewBox="0 0 856 40" aria-hidden="true">
    <rect x="0" y="5" width="856" height="35" fill="var(--navy)"/>
    <polygon points="425,5 856,5 856,22 440,22" fill="var(--stripe)"/>
  </svg>
</main>
</body>
</html>
```